Portrait Photographer Newsletter (www.lensbytheharbor.com)

We would like a newsletter that can be used in Mailwise Relay....you can visit our website to get some content....The main topics for the newsletter are 1. planning for your family portraits 2. We also offer restoration of your family heirlooms 3. Coming Soon.....www.dockandcottageguard.com (get content off our website.)
Misc:
Gift Certificates are available.
Click to schedule you appt today.
Mothers day.
I can provide more pictures but we really need the content of the news letter- we need a good writer...feel free to use info our of our website or be creative :)
We need help keeping up with email marketing if we find a fit, we would like to use find someone to help with this weekly or monthly
Target Market(s)
Family, middle to upper class
Industry/Entity Type
Portrait Photography
Designer to choose colors to be used in the design.

```html
<!DOCTYPE html>
<html lang="en">
<head>
<meta charset="utf-8">
<title>Lens by the Harbor Newsletter</title>
<link href="https://fonts.googleapis.com/css2?family=PT+Sans:wght@400;700&display=swap" rel="stylesheet">
<style>
  :root {
    --header-bg: #eeeef0;
    --band-blue: #0a67c1;
    --call-blue: #1b71bb;
    --button-blue: #0a88f5;
    --content-bg: #ededf0;
    --soft-bg: #f4f4f5;
    --heading: #363a40;
    --body: #6b6b6b;
    --rule: #dcdcdf;
    --accent-text: #2170bb;
    --muted: #9a9a9a;
    --white: #ffffff;
  }
  * { box-sizing: border-box; margin: 0; padding: 0; }
  html, body { width: 713px; height: 1200px; overflow: hidden; background: var(--white); }
  body { font-family: "PT Sans", Arial, sans-serif; }
  .newsletter { width: 713px; height: 1200px; position: relative; }

  .masthead { height: 75px; background: var(--header-bg); display: flex; align-items: center; padding-left: 12px; }
  .brand { display: flex; align-items: center; gap: 7px; font-size: 19px; color: #1f1f1f; font-weight: 400; }
  .brand-dot { width: 10px; height: 10px; background: #1f1f1f; border-radius: 50%; }
  .brand-divider { width: 1px; height: 60px; background: #cfcfd3; margin: 0 14px 0 16px; }
  .partner { display: flex; align-items: center; gap: 7px; font-size: 15px; font-weight: 700; color: #1f6fb8; }
  .partner-mark { width: 14px; height: 14px; border: 2px solid #1f6fb8; border-radius: 50%; }

  .hero-photo { height: 288px; background: linear-gradient(180deg, #8fa8b3 0%, #6f8a6a 35%, #4d5d66 70%, #e8e4df 100%); }

  .headline-band { height: 87px; background: var(--band-blue); display: flex; align-items: center; justify-content: center; }
  .headline-band h1 { color: var(--white); font-weight: 400; font-size: 27px; line-height: 33px; text-align: center; }

  .stories { height: 363px; background: var(--content-bg); padding: 20px 0 0 92px; }
  .story { width: 530px; }
  .story + .story { margin-top: 32px; }
  .story h2 { font-size: 15.5px; font-weight: 700; color: var(--heading); margin-left: 3px; padding-bottom: 8px; border-bottom: 1px solid var(--rule); width: 400px; }
  .story p { font-size: 12.5px; line-height: 21.4px; color: var(--body); margin: 8px 0 0 4px; }
  .read-more { display: inline-block; margin-top: 12px; width: 87px; height: 31px; line-height: 31px; text-align: center; border-radius: 16px; background: var(--button-blue); color: var(--white); font-size: 12.5px; text-decoration: none; }

  .restoration { height: 145px; background: var(--soft-bg); display: flex; align-items: center; justify-content: center; }
  .restoration p { color: var(--accent-text); font-size: 17px; line-height: 28.5px; text-align: center; }

  .call-band { height: 82px; background: var(--call-blue); color: var(--white); text-align: center; padding-top: 12px; }
  .call-band .call-label { font-size: 17.5px; font-weight: 700; line-height: 22px; }
  .call-band .call-number { font-size: 22px; font-weight: 700; line-height: 28px; }

  .contact-note { height: 97px; background: var(--white); text-align: center; padding-top: 14px; color: var(--body); font-size: 11.5px; line-height: 21.5px; }

  .footer { height: 63px; background: var(--soft-bg); display: flex; align-items: center; justify-content: space-between; padding: 0 98px 0 55px; }
  .footer small { font-size: 11px; color: var(--muted); }
  .social { display: flex; gap: 12px; }
  .social span { width: 12px; height: 12px; border-radius: 50%; background: #b4b4b8; }
</style>
</head>
<body>
<div class="newsletter">
  <header class="masthead">
    <div class="brand"><span class="brand-dot"></span>Lens by the Harbor</div>
    <div class="brand-divider"></div>
    <div class="partner"><span class="partner-mark"></span>Dock &amp; Cottage Guard</div>
  </header>

  <div class="hero-photo" role="img" aria-label="Photograph of a large extended family posing together outdoors by the water"></div>

  <section class="headline-band">
    <h1>Nothing says “family” like beautifully rendered beach<br>portraits that will be cherished for decades</h1>
  </section>

  <section class="stories">
    <article class="story">
      <h2>PLANNING FOR YOUR FAMILY PORTRAITS</h2>
      <p>Lorem ipsum dolor sit Lorem ipsum dolor sit Lorem ipsum dolor sit Lorem ipsum dolor sit Lorem ipsum dolor sit Lorem ipsum dolor sit Lorem ipsum dolor sit Lorem ipsum dolor sit</p>
      <a class="read-more" href="#">Read more</a>
    </article>
    <article class="story">
      <h2>GIFT CERTIFICATES ARE AVAILABLE.</h2>
      <p>Lorem ipsum dolor sit Lorem ipsum dolor sit Lorem ipsum dolor sit Lorem ipsum dolor sit Lorem ipsum dolor sit Lorem ipsum dolor sit Lorem ipsum dolor sit Lorem ipsum dolor sit Lorem ipsum dolor sit Lorem ipsum dolor sit Lorem ipsum dolor sit Lorem ipsum dolor sit Lorem ipsum</p>
      <a class="read-more" href="#">Read more</a>
    </article>
  </section>

  <section class="restoration">
    <p>We also offer restoration of your family heirlooms<br>Schedule an appointment with us to learn about how we can<br>protect your beach home while you are away</p>
  </section>

  <section class="call-band">
    <div class="call-label">LEARN MORE CALL TODAY</div>
    <div class="call-number">888-555-0142</div>
  </section>

  <section class="contact-note">
    <p>Please call us now for more information and reservations.<br>Local: 302-555-0178&nbsp; Toll Free: 888-555-0142</p>
  </section>

  <footer class="footer">
    <small>© copyright 2018 - Unsubscribe here</small>
    <div class="social" aria-label="Social links"><span></span><span></span><span></span></div>
  </footer>
</div>
</body>
</html>
```